We need visit card and a letter paper for our website. thx

We have a beauty clinic in Switzerland.
https://wolkenbachtal.ch
We need a visit card.

Requirements
Must have
• see colors on website

```html
<!DOCTYPE html>
<html lang="en">
<head>
<meta charset="utf-8">
<title>Wolkenbachtal Beauty Clinic – Business Cards</title>
<link rel="stylesheet" href="https://fonts.googleapis.com/css2?family=Josefin+Sans:wght@300;400;600&family=Quicksand:wght@400;500&display=swap">
<style>
  :root{
    --bg:#ebebeb;
    --card:#f7f7f7;
    --berry:#a64d78;
    --berry-light:#b9618b;
    --silver:#a9a9a9;
    --ink:#1c1c1c;
    --grey-text:#6d6d6d;
    --white:#ffffff;
  }
  *{box-sizing:border-box;margin:0;padding:0}
  html,body{width:1200px;height:720px;overflow:hidden;background:var(--bg)}
  body{position:relative;font-family:"Josefin Sans",sans-serif}

  .card{position:absolute;width:520px;height:300px;background:var(--card);overflow:hidden;
        box-shadow:0 2px 6px rgba(0,0,0,.12)}
  .card--front{left:50px;top:60px}
  .card--reminder{left:630px;top:360px;font-family:"Quicksand",sans-serif}

  /* front */
  .front-shape{position:absolute;inset:0}
  .brand{position:absolute;display:flex;align-items:center;gap:10px;color:var(--ink);
         font-family:"Josefin Sans",sans-serif;font-weight:300;letter-spacing:.5px;white-space:nowrap}
  .brand__square{width:12px;height:12px;border:1.5px solid var(--ink)}
  .card--front .brand{left:30px;top:134px;font-size:30px}
  .contact{position:absolute;right:30px;top:34px;text-align:right;color:var(--white);font-weight:300;white-space:nowrap}
  .contact__name{font-size:20px;font-weight:400;margin-bottom:18px}
  .contact__line{font-size:13px;line-height:20px;display:flex;justify-content:flex-end;align-items:center;gap:8px}
  .contact__gap{height:14px}
  .icon{width:15px;height:15px;flex:none}

  /* reminder */
  .card--reminder .brand{right:30px;top:26px;font-size:28px}
  .reminder__title{position:absolute;left:30px;top:86px;color:var(--berry);font-size:15px;letter-spacing:2.5px}
  .field{position:absolute;left:30px;display:flex;align-items:flex-end;gap:8px;color:var(--grey-text);
         font-size:13px;letter-spacing:1.5px}
  .field__rule{flex:1;border-bottom:1.5px solid var(--berry);height:1px}
  .field--name{top:112px;right:30px}
  .field--date{top:144px;right:30px}
  .field--purpose{top:176px;right:30px}
  .field__time{margin-left:14px}
  .days{position:absolute;left:30px;right:30px;top:204px;display:flex;justify-content:space-between;
        color:var(--grey-text);font-size:13px;letter-spacing:1.5px}
  .day{display:flex;align-items:center;gap:7px}
  .day__box{width:17px;height:17px;border:1.2px solid var(--berry)}
  .reminder__contact{position:absolute;left:30px;right:30px;top:234px;display:flex;justify-content:space-between;
        color:var(--grey-text);font-size:11px;letter-spacing:1px}
  .reminder__phone{display:flex;align-items:center;gap:5px}
  .footer-rule{position:absolute;left:0;right:0;top:253px;height:3px;background:var(--silver)}
  .footer-band{position:absolute;left:0;right:0;top:258px;bottom:0;background:var(--berry);color:var(--white);
        font-size:10.5px;line-height:14px;text-align:center;padding:7px 30px 0;letter-spacing:.3px}
</style>
</head>
<body>

<section class="card card--front" aria-label="Business card front">
  <svg class="front-shape" viewBox="0 0 520 300" width="520" height="300" aria-hidden="true">
    <path d="M220,0 C282,58 292,200 250,300 L520,300 L520,0 Z" fill="var(--berry-light)"/>
    <path d="M238,0 C298,62 306,204 264,300 L520,300 L520,0 Z" fill="var(--silver)"/>
    <path d="M250,0 C308,64 316,206 276,300 L520,300 L520,0 Z" fill="var(--berry)"/>
  </svg>

  <div class="brand"><span class="brand__square"></span>Wolkenbachtal</div>

  <div class="contact">
    <p class="contact__name">Dr. Lena Hartmann</p>
    <p class="contact__line">Talweg 14,</p>
    <p class="contact__line">7550 Scuol, Switzerland</p>
    <div class="contact__gap"></div>
    <p class="contact__line">+41 (0) 800 24 60 60
      <svg class="icon" viewBox="0 0 16 16"><circle cx="8" cy="8" r="8" fill="var(--white)"/><path d="M5 4.5l1.6-.5 1 2.2-1 .8c.5 1 1.2 1.7 2.2 2.2l.8-1 2.2 1-.5 1.6C8.5 11 5 7.5 5 4.5z" fill="var(--berry)"/></svg></p>
    <p class="contact__line">hallo@wolkenbachtal.ch
      <svg class="icon" viewBox="0 0 16 16"><circle cx="8" cy="8" r="8" fill="var(--white)"/><rect x="4" y="5.2" width="8" height="5.6" fill="none" stroke="var(--berry)" stroke-width="1"/><path d="M4 5.4l4 3 4-3" fill="none" stroke="var(--berry)" stroke-width="1"/></svg></p>
    <p class="contact__line">wolkenbachtal.ch
      <svg class="icon" viewBox="0 0 16 16"><circle cx="8" cy="8" r="8" fill="var(--white)"/><circle cx="8" cy="8" r="4" fill="none" stroke="var(--berry)" stroke-width="1"/><path d="M4 8h8M8 4c-2 2.5-2 5.5 0 8M8 4c2 2.5 2 5.5 0 8" fill="none" stroke="var(--berry)" stroke-width=".8"/></svg></p>
  </div>
</section>

<section class="card card--reminder" aria-label="Appointment reminder card">
  <div class="brand"><span class="brand__square"></span>Wolkenbachtal</div>
  <p class="reminder__title">Appointment Reminder</p>

  <div class="field field--name"><span>Patient`s Name:</span><span class="field__rule"></span></div>
  <div class="field field--date"><span>Date:</span><span class="field__rule"></span><span class="field__time">Time:</span><span class="field__rule"></span></div>
  <div class="field field--purpose"><span>Purpose:</span><span class="field__rule"></span></div>

  <div class="days">
    <span class="day">Mon <span class="day__box"></span></span>
    <span class="day">Tues <span class="day__box"></span></span>
    <span class="day">Wed <span class="day__box"></span></span>
    <span class="day">Thur <span class="day__box"></span></span>
    <span class="day">Fri <span class="day__box"></span></span>
  </div>

  <div class="reminder__contact">
    <span>7550 Scuol, Switzerland</span>
    <span class="reminder__phone">
      <svg class="icon" viewBox="0 0 16 16" width="12" height="12"><path d="M3 2l3-1 2 4-2 1.5c1 2 2.5 3.5 4.5 4.5L12 9l4 2-1 3C8 14 2 8 3 2z" fill="var(--berry)"/></svg>
      +41 (0) 800 24 60 60</span>
  </div>

  <div class="footer-rule"></div>
  <p class="footer-band">Please respect our time and that of other guests and give a 24 hr notice if you are not able to keep your appointment.</p>
</section>

</body>
</html>
```